Velmora Trade Hall (front page)

We need a design of a front page for our Velmora Trade Hall website (vth.co.uk). Our company is based in the United Kingdom and offers investors from all over the world an opportunity to invest into bitcoin and litecoin.

We have been developing this cutting edge technology for past 2 years based on our in depth knowledge on conventional stock and currency trading technology and methodology. We have run many test against penetration, security and stability and now are ready to deploy.

Recent news about vulnerability of such platforms leave a great deal of unease from retail investors about investing into cryptocurrency. We are set to challenge this attitude. Our background is payments in particular regulated environment in the UK. We are keen to apply our wealth of experience to provide secure and reliable trading platform and advance cryptocurrency as means of legal tender.

The front page should be based on the feel and look of our current technology vth.co.uk. Some of you have already been involved in logo design for our company, please see the attached mockups. The page should have this minimalist design, very clean and light.

Seek inspiration form www.korvelin.net, www.trusmarq.com, vip.plomwerth.com and other bitcoin exchanges.

We look forward to receiving your ideas.

You can also refer to our social pages:
https://www.facebook.com/vth.co.uk
https://twitter.com/vth_uk

We would like you to focus your efforts at designing the page in such a way so that it is very easy for visitor be open an account with the exchange. We must focus at informing the visitor about the bitcoin, how to my buy, how to sell, look at the general overview of the maker and CONVERTING him/her sing up. This is the most important!!

Regards,
Oren

Reason: Dear all, We are very keen on getting this design done right the first time. The key success is conversion of visitors to subscribers and then to traders. It is absolutely essential make the registration process as streamlined as possible! When we are calling them to act by "Change the world one bitcoin at a time" we should give them a opportunity to provide us with relevant account creation details: email, password, confirm password. Please visit quenzo.co.uk for ideas. Secondly, tell them what is a bitcoin, why a bitcoin is a good investment and how to invest. Finally, it is important to inform visitors of "who we are", what sets us apart from other exchanges, tell them about our experience. In our view graphs and live order books are important but they might turn some visitors away especially the ones that are not accustomed to online trading. Think of what would you like to see on the page if you wanted YOURSELF to invest. What would make you to create an account and use it? Think what will work, we are here to revolutionise how people do business.... any wild ideas put them to us. OUR BUDGET JUST GONE UP!!!

Target Market(s)

A combination of professional and consumer bitcoin investors.

Requirements
Must have
• News section

```html
<!DOCTYPE html>
<html lang="en">
<head>
<meta charset="utf-8">
<title>Velmora Trade Hall</title>
<link href="https://fonts.googleapis.com/css2?family=Ubuntu:wght@400;500;700&display=swap" rel="stylesheet">
<style>
:root{
  --ink:#2e2e2e;
  --blue:#1a9ad6;
  --blue-soft:#e6f3fb;
  --blue-head:#bfe1f5;
  --grey-band:#f2f2f2;
  --grey-row:#ebebeb;
  --grey-foot:#6e6e6e;
  --pink:#fbe6e6;
  --text:#222;
  --muted:#8a8a8a;
}
*{box-sizing:border-box;margin:0;padding:0}
html,body{width:1200px;height:841px;overflow:hidden;background:#fff}
body{font-family:"Ubuntu",sans-serif;color:var(--text)}
a{color:inherit;text-decoration:none}
.stage{position:relative;width:1360px;height:953px;transform:scale(.88235);transform-origin:0 0}
.stage > *{position:absolute}

/* header */
.topbar{left:0;top:0;width:1360px;height:88px;background:var(--ink)}
.topbar-rule{left:0;top:88px;width:1360px;height:6px;background:var(--blue)}
.brand-name{left:20px;top:58px;color:#fff;font-size:16px;font-weight:400;letter-spacing:1px;white-space:nowrap}
.login{left:961px;top:12px;display:flex;gap:19px}
.login-field{width:152px;height:27px;border:1px dashed #9a9a9a;border-radius:3px;color:#fff;font-size:11px;padding:7px 9px}
.go-btn{left:1297px;top:12px;width:50px;height:27px;background:var(--blue);color:#fff;font-size:14px;text-align:center;line-height:27px;border-radius:2px}
.lang{left:1255px;top:51px;width:92px;height:26px;background:#fff;border-radius:2px;color:var(--blue);font-size:12px;padding:6px 8px}
.lang svg{position:absolute;right:8px;top:10px}

/* nav band */
.navband{left:0;top:94px;width:1360px;height:64px;background:var(--grey-band);border-bottom:1px solid #ddd}
.nav-active{left:36px;top:109px;width:92px;height:34px;background:var(--blue);color:#fff;font-size:14px;text-align:center;line-height:34px;border-radius:2px}
.nav-link{top:119px;font-size:14px;color:var(--text)}
.tagline{left:520px;top:100px;width:435px;height:50px;background:linear-gradient(90deg,#ececec,#e2e2e2,#ececec);border-radius:4px}
.account-links{left:1156px;top:117px;display:flex;gap:18px;font-size:13px;color:var(--blue)}

/* market list */
.markets{left:13px;top:170px;width:240px;height:258px;background:var(--grey-row);border-radius:8px;overflow:hidden}
.markets-tabs{display:flex;height:43px;border-bottom:2px solid var(--blue);background:#fff}
.markets-tab{flex:1;text-align:center;line-height:43px;font-size:14px;color:var(--blue)}
.markets-tab.is-on{background:var(--blue);color:#fff;border-radius:8px 8px 0 0}
.pair{display:flex;align-items:center;height:32px;border-top:1px solid #fff;font-size:12.5px;padding-left:8px}
.pair-star{color:var(--blue);width:17px;font-size:12px}
.pair-name{width:67px}
.pair-spark{width:51px;height:21px;background:#fff;border-top:1px solid var(--blue-head);border-bottom:1px solid var(--blue-head);margin-right:20px}

/* tweets */
.tweets{left:13px;top:448px;width:240px;height:340px;background:var(--blue);border-radius:8px 8px 0 0}
.follow{left:13px;top:786px;width:143px;height:31px;background:var(--blue);clip-path:polygon(0 0,100% 0,85% 100%,0 100%);border-radius:0 0 0 8px;color:#fff;font-size:14px;padding:4px 24px}
.tweets-title{left:26px;top:460px;color:#fff;font-size:13px;font-weight:500}
.tweet{left:19px;width:224px;background:#fff;border-radius:3px;padding:10px 12px;font-size:10.5px;line-height:14px}
.tweet::before{content:"";position:absolute;left:18px;top:-14px;border:14px solid transparent;border-top:0;border-bottom-color:#fff}
.tweet:first-of-type::before{display:none}
.tweet-head{display:flex;align-items:center;gap:8px;color:var(--blue);font-size:10.5px;padding-bottom:7px;margin-bottom:8px;border-bottom:1px dashed #ccc}
.tweet-dot{width:11px;height:11px;border-radius:50%;background:var(--blue)}

/* chart panel */
.chart-panel{left:269px;top:170px;width:776px;height:460px;background:var(--blue-soft);border:1px solid #cde3f2;border-radius:4px}
.view-dot{width:94px;height:94px;border-radius:50%;background:var(--ink);color:var(--blue);font-size:14px;text-align:center;line-height:94px;top:183px}
.view-dot.is-on{background:var(--blue);color:#fff;font-weight:500}
.view-pointer{left:348px;top:268px}
.chart-card{left:293px;top:300px;width:729px;height:307px;background:#fff}
.frames{left:305px;top:317px;display:flex;border:1px solid #999;font-size:11.5px}
.frames span{padding:2px 3px;border-right:1px solid #999}
.frames span:last-child{border-right:0}
.frames .is-on{background:#fff7c8}
.chart-title{left:628px;top:320px;font-size:12.5px;font-weight:500}
.axis-y{left:305px;font-size:12px;color:#444}
.axis-x{top:558px;font-size:11px;color:#555}
.plot{left:293px;top:300px}

/* orders */
.order-tab{top:639px;width:246px;height:38px;background:var(--ink);color:#fff;font-size:15px;font-weight:500;text-align:center;line-height:38px}
.order-tab.is-on{background:var(--blue)}
.order-pointer{left:381px;top:676px}
.orders{left:269px;top:700px;width:772px;border-collapse:collapse;font-size:11.5px}
.orders th{background:var(--blue-head);font-weight:400;font-size:13.5px;height:28px;text-align:left;padding-left:20px}
.orders td{height:28px;padding-left:18px}
.orders tr:nth-child(even) td{background:#eef7fd}
.orders tbody tr:last-child td{border-bottom:6px solid #eef7fd}

/* order book */
.book{left:1059px;top:170px;width:290px;border-collapse:collapse;font-size:12.5px;color:var(--muted)}
.book th{background:var(--ink);color:#fff;height:43px;font-size:14px;font-weight:500;border-right:1px solid #555}
.book th:first-child{border-radius:8px 0 0 0}
.book th:last-child{border-radius:0 8px 0 0;border-right:0}
.book td{height:30px;text-align:center;border-right:1px solid #d5d5d5;border-bottom:1px solid #fff}
.book .ask-row td{background:var(--blue-soft)}
.book .ask-row td:first-child{background:#f0f0f0}
.book .bid-row td{background:var(--pink)}
.book .bid-row td:last-child{background:#f3f3f3}
.book-foot{left:1059px;top:487px;width:290px;height:8px;background:#e2e2e2}

/* trade form */
.trade-tab{top:521px;width:146px;height:41px;text-align:center;font-size:13px;font-weight:500;line-height:18px;padding-top:3px;border-radius:3px 3px 0 0}
.trade-tab.is-on{left:1056px;background:var(--blue);color:#fff}
.trade-tab.is-off{left:1202px;background:#e2e2e2;color:#fff}
.trade-form{left:1056px;top:562px;width:294px;height:252px;border:2px solid var(--blue);border-radius:0 0 5px 5px}
.form-label{left:1074px;font-size:12px;color:#444}
.form-input{left:1167px;width:170px;height:28px;border:1px solid #bbb;border-radius:4px;background:linear-gradient(#fff,#e3e3e3 40%)}
.form-btn{top:752px;width:124px;height:32px;color:#fff;font-size:15px;font-weight:500;text-align:center;line-height:32px}
.commission{left:1058px;top:794px;width:290px;text-align:center;font-size:10.5px;font-family:Arial,sans-serif}

/* footer */
.footer-links{left:0;top:848px;width:1360px;height:52px;background:#e8f3fb;display:flex;justify-content:center;align-items:center;gap:40px;font-size:13px}
.footer-base{left:0;top:900px;width:1360px;height:53px;background:var(--grey-foot);color:#fff;font-size:13px;text-align:center;line-height:56px}
</style>
</head>
<body>
<div class="stage">

  <header class="topbar"></header>
  <div class="topbar-rule"></div>
  <div class="brand-name">Velmora Trade Hall</div>
  <form class="login"><div class="login-field">Email :</div><div class="login-field">Password :</div></form>
  <div class="go-btn">GO</div>
  <div class="lang">English<svg width="10" height="6"><path d="M0 0h10L5 6z" fill="#1a9ad6"/></svg></div>

  <nav class="navband"></nav>
  <a class="nav-active" href="#">Overview</a>
  <a class="nav-link" href="#" style="left:165px">Who We Are</a>
  <a class="nav-link" href="#" style="left:300px">News</a>
  <div class="tagline" role="img" aria-label="Hand-lettered slogan: Change the world one bitcoin at a time"></div>
  <div class="account-links"><a href="#">Sign Up</a><span>|</span><a href="#">Forgot password?</a></div>

  <section class="markets">
    <div class="markets-tabs"><div class="markets-tab is-on">ALL</div><div class="markets-tab">FAVS</div></div>
    <div style="height:7px;background:#fff"></div>
    <div class="pair"><span class="pair-star">★</span><span class="pair-name">BTC/USD</span><span class="pair-spark"></span>566.5900</div>
    <div class="pair"><span class="pair-star">★</span><span class="pair-name">LTC/USD</span><span class="pair-spark"></span>15.8000</div>
    <div class="pair"><span class="pair-star">★</span><span class="pair-name">EUR/USD</span><span class="pair-spark"></span>1.3810</div>
    <div class="pair"><span class="pair-star">★</span><span class="pair-name">LTC/BTC</span><span class="pair-spark"></span>0.0277</div>
    <div class="pair"><span class="pair-star">★</span><span class="pair-name">BTC/EUR</span><span class="pair-spark"></span>411.0700</div>
    <div class="pair"><span class="pair-star">★</span><span class="pair-name">LTC/EUR</span><span class="pair-spark"></span>11.4000</div>
  </section>

  <section class="tweets"></section>
  <div class="tweets-title">Tweets</div>
  <article class="tweet" style="top:490px;height:102px"><div class="tweet-head"><span class="tweet-dot"></span>VTH @vth_uk</div>Velmora Trade Hall is a powerful and secure cryptocurrency trading platform designed for retail and institutional investors.</article>
  <article class="tweet" style="top:612px;height:72px"><div class="tweet-head"><span class="tweet-dot"></span>VTH @vth_uk</div>Change the world one bitcoin at a time.</article>
  <article class="tweet" style="top:706px;height:72px"><div class="tweet-head"><span class="tweet-dot"></span>VTH @vth_uk</div>Change the world one bitcoin at a time.</article>
  <div class="follow">Follow Us</div>

  <section class="chart-panel"></section>
  <svg class="view-pointer" width="30" height="30"><path d="M0 0h30L15 28z" fill="#1a9ad6"/></svg>
  <div class="view-dot is-on" style="left:315px">QUOTE</div>
  <div class="view-dot" style="left:513px">SCANDLES</div>
  <div class="view-dot" style="left:702px">DEPTH</div>
  <div class="view-dot" style="left:887px">VOLUME</div>
  <div class="chart-card"></div>
  <svg class="plot" width="729" height="307" viewBox="293 300 729 307">
    <defs><linearGradient id="area" x1="0" y1="0" x2="0" y2="1"><stop offset="0" stop-color="#bfe0f4"/><stop offset="1" stop-color="#fff"/></linearGradient></defs>
    <g stroke="#eee"><line x1="350" y1="370" x2="1012" y2="370"/><line x1="350" y1="431" x2="1012" y2="431"/><line x1="350" y1="493" x2="1012" y2="493"/></g>
    <path fill="url(#area)" d="M350 388L360 418L368 405L382 385L392 395L402 418L415 410L430 400L440 408L448 395L460 405L470 395L485 410L500 402L518 422L530 412L545 398L555 405L568 408L585 388L598 425L610 420L620 435L630 462L642 480L652 490L665 492L675 500L685 485L697 495L708 520L720 492L730 503L740 490L752 500L765 503L778 470L790 473L800 488L810 475L822 460L832 435L842 398L850 418L860 402L868 415L876 425L890 430L905 435L918 400L930 398L950 398L958 392L968 410L978 395L990 400L1000 418L1010 435L1010 530L350 530Z"/>
    <polyline fill="none" stroke="#3aa3dc" stroke-width="1.2" points="350,388 360,418 368,405 382,385 392,395 402,418 415,410 430,400 440,408 448,395 460,405 470,395 485,410 500,402 518,422 530,412 545,398 555,405 568,408 585,388 598,425 610,420 620,435 630,462 642,480 652,490 665,492 675,500 685,485 697,495 708,520 720,492 730,503 740,490 752,500 765,503 778,470 790,473 800,488 810,475 822,460 832,435 842,398 850,418 860,402 868,415 876,425 890,430 905,435 918,400 930,398 950,398 958,392 968,410 978,395 990,400 1000,418 1010,435"/>
  </svg>
  <div class="frames"><span>M1</span><span class="is-on">M5</span><span>M15</span><span>M30</span><span>H1</span><span>H4</span></div>
  <div class="chart-title">BTC/USD</div>
  <div class="axis-y" style="top:360px">569.300</div>
  <div class="axis-y" style="top:420px">567</div>
  <div class="axis-y" style="top:482px">564.6</div>
  <div class="axis-x" style="left:451px">16:10</div>
  <div class="axis-x" style="left:563px">17:00</div>
  <div class="axis-x" style="left:675px">17:50</div>
  <div class="axis-x" style="left:787px">18:40</div>
  <div class="axis-x" style="left:899px">19:30</div>

  <div class="order-tab is-on" style="left:269px">Active orders</div>
  <svg class="order-pointer" width="26" height="14"><path d="M0 0h26L13 13z" fill="#1a9ad6"/></svg>
  <div class="order-tab" style="left:534px">All orders</div>
  <div class="order-tab" style="left:797px">Trade history</div>
  <table class="orders">
    <thead><tr><th>Market</th><th>Time</th><th>Type</th><th>Volume (BTC)</th><th>Price</th><th>Total (USD)</th></tr></thead>
    <tbody>
      <tr><td>BTC/USD</td><td>3/25/2014 11:29:13 PM</td><td>Sell</td><td>1.15948</td><td>577</td><td>669.0200</td></tr>
      <tr><td>BTC/USD</td><td>3/25/2014 11:27:01 PM</td><td>Sell</td><td>0.00896</td><td>577.1</td><td>5.1708</td></tr>
      <tr><td>BTC/USD</td><td>3/25/2014 11:25:49 PM</td><td>Buy</td><td>0.00802</td><td>577</td><td>4.6275</td></tr>
    </tbody>
  </table>

  <table class="book">
    <thead><tr><th style="width:89px">BID</th><th style="width:102px">PRICE</th><th>ASK</th></tr></thead>
    <tbody>
      <tr class="ask-row"><td></td><td>579.00000</td><td>0.03711</td></tr>
      <tr class="ask-row"><td></td><td>578.99900</td><td>0.00641</td></tr>
      <tr class="ask-row"><td></td><td>578.69900</td><td>0.02358</td></tr>
      <tr class="ask-row"><td></td><td>578.50000</td><td>12.52873</td></tr>
      <tr class="ask-row"><td></td><td>578.46300</td><td>0.99432</td></tr>
      <tr class="bid-row"><td>5.49597</td><td>577.00000</td><td></td></tr>
      <tr class="bid-row"><td>0.530395</td><td>76.20000</td><td></td></tr>
      <tr class="bid-row"><td>1.838715</td><td>76.00200</td><td></td></tr>
      <tr class="bid-row"><td>0.530395</td><td>76.20000</td><td></td></tr>
    </tbody>
  </table>
  <div class="book-foot"></div>

  <div class="trade-tab is-on">Buy BTC<br>577.69900 USD</div>
  <div class="trade-tab is-off">Sell BTC<br>577.00000 USD</div>
  <section class="trade-form"></section>
  <div class="form-label" style="top:584px">Type</div>
  <div class="form-input" style="top:575px"></div>
  <div class="form-label" style="top:620px">Volume BTC</div>
  <div class="form-input" style="top:611px;background:#e3e3e3"></div>
  <div class="form-label" style="top:656px">Price per BTC</div>
  <div class="form-input" style="top:648px"></div>
  <div class="form-label" style="top:692px">TotalFee</div>
  <div class="form-label" style="top:692px;left:1171px">Fee</div>
  <div class="form-label" style="top:728px">USD 0.0000</div>
  <div class="form-label" style="top:728px;left:1169px">USD 0.00000</div>
  <div class="form-btn" style="left:1071px;background:var(--blue)">Sell BTC</div>
  <div class="form-btn" style="left:1209px;width:125px;background:#b5b5b5">Cancel</div>
  <div class="commission">Commission for the transaction is 0.2%</div>

  <footer class="footer-links"><span>HOME</span><span>|</span><span>API TRADE</span><span>|</span><span>TERMS AND CONDITIONS</span><span>|</span><span>CONTACTS</span><span>|</span><span>SUPPORT</span></footer>
  <div class="footer-base">© 2014 Velmora Trade Hall Limited. All rights reserved</div>

</div>
</body>
</html>
```